Business Card - Professional Minimalist - Double sided

We appreciate minimalist logo/web/collateral designs that allow design to tell a story. We want to relay a professional image/approach but throwing in a splash of modern when we’re able so long as it’s not distracting. Think 75% classic corporate, 25% modern. Open to black or white design, not sure which might look the best.

Target Market(s)

Senior executives or related government affairs contacts within the agriculture, energy, and defense industries (i.e., potential clients) but located outside of Washington, DC. Most potential clients based in DC with be familiar with both of us and our shared history.

Industry/Entity Type

Consulting

Contact Information for Business Card

Name: Daniel R. Whitlock
Title: Co-Founder & Partner
Address: 418 Bramblewood Ave. SE | Suite 2716 | Washington, D.C. 20019
Phone: (202) 555-0187
Email: Daniel@HollerbyWhitlock.com

Font styles to use
Serif

Colors

Designer to choose only greyscale colors for use in the design.

Requirements
Must have
• Name: Daniel R. Whitlock
Phone: (202) 555-0187

```html
<!DOCTYPE html>
<html lang="en">
<head>
<meta charset="utf-8">
<title>Hollerby Whitlock Group – Business Card</title>
<link href="https://fonts.googleapis.com/css2?family=Tinos:wght@400;700&display=swap" rel="stylesheet">
<style>
  :root{
    --stage:#8d8d8d;
    --card:#2b2b2b;
    --card-deep:#1c1c1c;
    --edge:#cfcfcf;
    --brand:#8a8a8a;
    --ink:#e6e6e6;
    --ink-soft:#c4c4c4;
    --rule:#6f6f6f;
  }
  *{box-sizing:border-box;margin:0;padding:0}
  html,body{width:1200px;height:900px;overflow:hidden}
  body{
    background:var(--stage);
    font-family:"Tinos","Times New Roman",serif;
    display:flex;flex-direction:column;align-items:center;justify-content:center;gap:50px;
  }
  .card{
    width:580px;height:332px;border-radius:22px;
    border:3px solid var(--edge);
    background:var(--card);
    position:relative;overflow:hidden;
  }
  /* back side */
  .card--back{background:var(--card-deep)}
  .card--back .texture{
    position:absolute;inset:0;
    background:linear-gradient(135deg,#262626 0%,#1a1a1a 50%,#242424 100%);
  }
  .card--back .brand{
    position:absolute;left:50%;top:50%;transform:translate(-50%,-50%);
    text-align:center;
  }
  /* brand lockup */
  .brand{color:var(--brand);font-weight:400;text-transform:uppercase}
  .brand__mark{width:46px;height:46px;border:3px solid var(--brand);margin:0 auto 18px}
  .brand__name{font-size:30px;letter-spacing:1px;line-height:1}
  .brand__rule{height:1px;background:var(--rule);margin:8px 0 6px}
  .brand__sub{font-size:13px;letter-spacing:9px;text-align:right}
  /* front side */
  .card--front .brand{position:absolute;left:34px;top:64px;width:240px;text-align:center}
  .card--front .brand__name{font-size:22px}
  .card--front .brand__mark{width:40px;height:40px}
  .card--front .brand__sub{font-size:11px;letter-spacing:7px}
  .divider{
    position:absolute;left:292px;top:40px;width:2px;height:250px;
    background:linear-gradient(to bottom,transparent,#9a9a9a 45%,transparent);
  }
  .contact{position:absolute;left:318px;top:52px;color:var(--ink-soft)}
  .contact__name{font-size:25px;font-weight:700;color:var(--ink)}
  .contact__title{font-size:16px;margin:2px 0 16px}
  .contact__row{display:flex;align-items:flex-start;gap:10px;font-size:15px;line-height:1.35;margin-bottom:6px}
  .contact__row svg{flex:none;width:16px;height:16px;margin-top:2px;fill:var(--ink-soft)}
</style>
</head>
<body>
  <section class="card card--back" aria-label="Card back">
    <div class="texture" role="img" aria-label="Subtle dark diamond background pattern"></div>
    <div class="brand">
      <div class="brand__mark"></div>
      <div class="brand__name">Hollerby Whitlock</div>
      <div class="brand__rule"></div>
      <div class="brand__sub">Group</div>
    </div>
  </section>

  <section class="card card--front" aria-label="Card front">
    <div class="brand">
      <div class="brand__mark"></div>
      <div class="brand__name">Hollerby Whitlock</div>
      <div class="brand__rule"></div>
      <div class="brand__sub">Group</div>
    </div>
    <div class="divider"></div>
    <div class="contact">
      <div class="contact__name">Daniel R. Whitlock</div>
      <div class="contact__title">Co-Founder &amp; Partner</div>
      <div class="contact__row">
        <svg viewBox="0 0 16 16"><rect x="0" y="0" width="16" height="16" rx="3"/><path d="M5 3.5l2 2-1 1.2c.6 1.3 1.6 2.3 2.8 2.8L10 8.5l2 2-1.3 1.6C7.4 11.8 4.2 8.6 3.9 5.3z" fill="#2b2b2b"/></svg>
        <span>(202) 555-0187</span>
      </div>
      <div class="contact__row">
        <svg viewBox="0 0 16 16"><rect x="0" y="3" width="16" height="11" rx="1"/><path d="M0.5 3.5L8 9.5l7.5-6" stroke="#2b2b2b" stroke-width="1.4" fill="none"/></svg>
        <span>Daniel@HollerbyWhitlock.com</span>
      </div>
      <div class="contact__row">
        <svg viewBox="0 0 16 16"><path d="M8 0a5.5 5.5 0 0 0-5.5 5.5C2.5 10 8 16 8 16s5.5-6 5.5-10.5A5.5 5.5 0 0 0 8 0z"/><circle cx="8" cy="5.5" r="2" fill="#2b2b2b"/></svg>
        <span>418 Bramblewood Ave. SE |<br>Suite 2716 |<br>Washington, D.C. 20019</span>
      </div>
    </div>
  </section>
</body>
</html>
```